Brightwave Reach - Business Card

We need a business card for a Social Media Marketing company that specializes in online marketing for small businesses in Canada using common Social Media platforms such as Pictora, Kinloop, Glintbox & Chirpo.

I have uploaded a copy of our logo which I would like utilized in the business card. We would like the business card to be modern yet classy design.

Our website is www.brightwavereach.ca

Industry/Entity Type

Marketing

Contact Information for Business Card

Email: info@brightwavereach.ca
Website: www.brightwavereach.ca
Telephone: 604-392-5108

Colors

Designer to choose colors to be used in the design.

Requirements
Must have
• Social Media icons on reverse
• Please add some designs with color.

```html
<!DOCTYPE html>
<html lang="en">
<head>
<meta charset="UTF-8">
<title>Brightwave Reach – Business Card</title>
<link rel="stylesheet" href="https://fonts.googleapis.com/css2?family=Lato:wght@400;700;900&display=swap">
<style>
  :root {
    --stage: #e4e4e4;
    --card-white: #ffffff;
    --card-black: #0b0b0b;
    --ink: #2e2e2e;
    --ink-soft: #555555;
    --rule: #3a3a3a;
    --band: #4a4a4a;
    --band-light: #9a9a9a;
    --white: #ffffff;
  }
  * { box-sizing: border-box; margin: 0; padding: 0; }
  html, body { width: 1200px; height: 680px; overflow: hidden; }
  body {
    background: var(--stage);
    font-family: "Lato", Arial, sans-serif;
    position: relative;
  }
  .card {
    position: absolute;
    top: 197px;
    width: 500px;
    height: 286px;
    border-radius: 4px;
    box-shadow: 0 10px 28px rgba(0,0,0,0.22);
    overflow: hidden;
  }
  .card--front { left: 60px; background: var(--card-white); color: var(--ink); }
  .card--back { left: 640px; background: var(--card-black); color: var(--white); }

  /* front */
  .front-band { position: absolute; left: 0; bottom: 0; width: 500px; height: 40px; }
  .brand {
    position: absolute;
    display: flex;
    align-items: center;
    gap: 10px;
  }
  .brand__square { width: 18px; height: 18px; background: currentColor; flex: none; }
  .brand__name {
    font-weight: 900;
    text-transform: uppercase;
    letter-spacing: 0.04em;
    line-height: 1.05;
  }
  .card--front .brand { left: 40px; top: 92px; color: var(--ink); }
  .card--front .brand__name { font-size: 22px; }

  .holder { position: absolute; right: 40px; top: 58px; text-align: right; }
  .holder__name { font-size: 19px; font-weight: 700; color: var(--ink); }
  .holder__role { font-size: 11px; color: var(--ink-soft); margin-top: 2px; }
  .rule { position: absolute; height: 1px; background: var(--rule); }
  .rule--top { right: 40px; top: 104px; width: 200px; }
  .rule--bottom { left: 40px; top: 190px; width: 190px; }

  .contact { display: flex; align-items: center; gap: 8px; font-size: 12.5px; color: var(--ink); }
  .contact svg { width: 11px; height: 11px; flex: none; }
  .contact--web { position: absolute; right: 40px; top: 122px; }
  .contact-list { position: absolute; left: 40px; top: 202px; display: flex; flex-direction: column; gap: 5px; }

  /* back */
  .card--back .brand {
    left: 50%; top: 74px; transform: translateX(-50%);
    flex-direction: column; gap: 10px; text-align: center;
  }
  .card--back .brand__square { width: 16px; height: 16px; }
  .card--back .brand__name { font-size: 28px; }
  .platforms {
    position: absolute; left: 0; right: 0; bottom: 46px;
    display: flex; justify-content: center; gap: 26px;
    list-style: none;
  }
  .platform { display: flex; align-items: center; gap: 6px; font-size: 12px; font-weight: 700; }
  .platform__square { width: 12px; height: 12px; background: var(--white); border-radius: 2px; }
</style>
</head>
<body>

<section class="card card--front" aria-label="Business card front">
  <div class="brand">
    <span class="brand__square"></span>
    <span class="brand__name">Brightwave<br>Reach</span>
  </div>

  <div class="holder">
    <p class="holder__name">Daniel Ashford</p>
    <p class="holder__role">Manager</p>
  </div>
  <div class="rule rule--top"></div>

  <p class="contact contact--web">
    <svg viewBox="0 0 12 12" fill="none" stroke="#3a3a3a" stroke-width="1"><circle cx="6" cy="6" r="5"/><ellipse cx="6" cy="6" rx="2.2" ry="5"/><line x1="1" y1="6" x2="11" y2="6"/></svg>
    www.brightwavereach.ca
  </p>

  <div class="rule rule--bottom"></div>
  <div class="contact-list">
    <p class="contact">
      <svg viewBox="0 0 12 12"><path fill="#2e2e2e" d="M2.4 1l2 2.2-1 1.3c.7 1.6 1.9 2.8 3.5 3.5l1.3-1 2.2 2-1.2 1.8C5.6 10.6 1.4 6.4 1 2.2z"/></svg>
      604-392-5108
    </p>
    <p class="contact">
      <svg viewBox="0 0 12 12" fill="none" stroke="#2e2e2e" stroke-width="1.1"><rect x="1" y="2.5" width="10" height="7"/><path d="M1 2.5l5 4 5-4"/></svg>
      info@brightwavereach.ca
    </p>
  </div>

  <svg class="front-band" viewBox="0 0 500 40" preserveAspectRatio="none">
    <polygon points="0,40 0,30 330,30 346,14 500,14 500,40" fill="#9a9a9a"/>
    <polygon points="0,40 0,33 334,33 350,17 500,17 500,40" fill="#4a4a4a"/>
  </svg>
</section>

<section class="card card--back" aria-label="Business card back">
  <div class="brand">
    <span class="brand__square"></span>
    <span class="brand__name">Brightwave<br>Reach</span>
  </div>
  <ul class="platforms">
    <li class="platform"><span class="platform__square"></span>Kinloop</li>
    <li class="platform"><span class="platform__square"></span>Pictora</li>
    <li class="platform"><span class="platform__square"></span>Chirpo</li>
    <li class="platform"><span class="platform__square"></span>Glintbox</li>
  </ul>
</section>

</body>
</html>
```